need a Flyer for Plush Toy company

Need a Flyer for Plush Toy company ,

I upload a file for TEXT

Target Market(s)

Toys wholesalers , Supermarket

Industry/Entity Type

Toy Store

Colors
000000
ec1f27
c4c4c4

Requirements
Must have
• I have up loaded 3 files
• 1. Logo Registered Brand
• 2. customer's design in drawing
• 3. our ready samples based on Design
Nice to have
• happy kids in Nature ,
• happy kids in Ski ,
• different color Kids ,
• Multi culture concept

```html
<!DOCTYPE html>
<html lang="en">
<head>
<meta charset="utf-8">
<title>Momo Pui – Plush Toy Flyer</title>
<link rel="stylesheet" href="https://fonts.googleapis.com/css2?family=Source+Sans+3:ital,wght@0,400;0,600;0,700;1,400;1,600&family=Patrick+Hand&display=swap">
<style>
  :root {
    --red: #ec1f27;
    --red-deep: #c8141b;
    --black: #000000;
    --ink: #333333;
    --grey: #c4c4c4;
    --paper: #ffffff;
    --backdrop: #e9e6e2;
    --grass: #4e9a2a;
    --grass-light: #6cbf3a;
  }
  * { box-sizing: border-box; margin: 0; padding: 0; }
  html, body { width: 1200px; height: 943px; overflow: hidden; }
  body {
    background: var(--backdrop);
    font-family: "Source Sans 3", sans-serif;
    color: var(--ink);
    display: flex; align-items: center; justify-content: center;
  }
  .flyer {
    position: relative;
    width: 640px; height: 905px;
    background: var(--red);
    padding: 26px 26px 0 26px;
    box-shadow: 0 6px 24px rgba(0,0,0,.25);
    overflow: hidden;
  }
  .flyer__sheet {
    position: relative;
    background: var(--paper);
    height: 100%;
    padding: 24px 34px 0;
    display: flex; flex-direction: column;
  }
  .masthead { display: flex; justify-content: space-between; align-items: flex-start; height: 200px; flex-shrink: 0; }
  .masthead__emblem { display: flex; flex-direction: column; align-items: center; width: 230px; padding-top: 6px; }
  .emblem-art { width: 130px; height: 130px; background: linear-gradient(180deg,#f4f4f4,#d9d9d9); border-radius: 6px; }
  .tagline { font-family: "Patrick Hand", cursive; color: var(--red); font-size: 26px; margin-top: 6px; }
  .brand-name {
    font-weight: 700; color: var(--red); font-size: 84px; line-height: .95;
    text-align: right; margin-top: 10px;
  }
  .intro { text-align: center; margin-top: 6px; }
  .intro__title { font-style: italic; font-size: 26px; color: #444; font-weight: 600; line-height: 1.2; }
  .intro__sub { color: var(--red); font-weight: 600; font-size: 16px; line-height: 1.25; margin-top: 4px; }
  .samples { width: 380px; height: 120px; margin: 12px auto 10px; border-radius: 10px; flex-shrink: 0;
    background: linear-gradient(90deg,#f4b6c8,#f6f0e8 30%,#f3a13b 45%,#b8a6e0 62%,#6aa7d4 78%,#f4d23a); }
  .copy { font-size: 12px; line-height: 1.45; color: #444; }
  .copy p { margin-bottom: 5px; }
  .copy .centered { text-align: center; }
  .address { text-align: center; font-weight: 700; font-size: 15px; line-height: 1.3; color: #222; margin: 6px 0 10px; }
  .details { display: flex; justify-content: space-between; font-size: 12px; line-height: 1.4; color: #333; }
  .details b { font-weight: 700; }
  .details__contact { text-align: left; }
  .footer { position: relative; margin: auto -60px 0; height: 185px; flex-shrink: 0; }
  .footer__art { position: absolute; left: 50%; top: 0; transform: translateX(-50%); width: 340px; height: 100px; border-radius: 12px;
    background: linear-gradient(180deg,#cfe6b9,#a9d08a); }
  .footer__grass { position: absolute; left: 0; right: 0; bottom: 0; width: 100%; height: 110px; }
  .ribbon { position: absolute; left: 50%; top: 92px; transform: translateX(-50%) rotate(2deg);
    background: var(--red-deep); color: #fff; font-weight: 700; font-size: 16px;
    padding: 6px 18px; white-space: nowrap; box-shadow: 0 2px 4px rgba(0,0,0,.25); }
  .phone { position: absolute; left: 0; right: 0; top: 142px; text-align: center; color: #fff; font-weight: 700; font-size: 15px;
    display: flex; align-items: center; justify-content: center; gap: 8px; }
</style>
</head>
<body>
  <article class="flyer">
    <div class="flyer__sheet">
      <header class="masthead">
        <div class="masthead__emblem">
          <div class="emblem-art" role="img" aria-label="Line drawing of two children on a pirate ship"></div>
          <p class="tagline">Have you been there?</p>
        </div>
        <div class="brand-name">Momo<br>Pui</div>
      </header>

      <section class="intro">
        <h1 class="intro__title">Einzelunternehmen / Family business</h1>
        <p class="intro__sub">Innovative Developer for Plush Toys<br>International Trader for Toys</p>
      </section>

      <div class="samples" role="img" aria-label="Photo of a row of plush toy samples: rabbit, owl, lion, elephant, bird and chick"></div>

      <section class="copy">
        <p class="centered">We live and work in Kerpen near to Cologne Germany. We speak German and English.</p>
        <p>The toys are made in China, we are small family business, but we are professional in Plush toys business, right now we have successfully launched Projects with a huge Japanese 100 Yen Chain Store. Here in Flyer we show a Sample project.</p>
        <p>100 Yen = 0.90 USD , Our products can meet strictest Quality Control , but are with extremely Low Price to fit for Japanese Dollar Shop as well as his overseas Store around the world.</p>
      </section>

      <p class="address">Lindenweg 8, 50171 Kerpen Germany</p>

      <section class="details">
        <div class="details__bank">
          <b>Bank information</b><br>
          <b>Kontoinhaber/Account Holder :</b> Lena Park<br>
          <b>IBAN :</b> DE12 3456 7890 1234 5678 00<br>
          <b>BIC :</b> EXMPDEFF123
        </div>
        <div class="details__contact">
          <b>hello@momopui-toys.de</b><br>
          <b>Fon</b> +49 (0) 2237- 555 0142<br>
          <b>Fax</b> +49 (0) 2237- 555 0143<br>
          <b>Ust-IdNr./VAT No.</b> DE123456789
        </div>
      </section>

      <footer class="footer">
        <svg class="footer__grass" viewBox="0 0 640 110" preserveAspectRatio="none" aria-hidden="true">
          <path d="M0 30 Q40 6 80 26 Q120 4 170 24 Q230 8 290 28 Q350 6 410 24 Q470 4 530 26 Q590 8 640 22 L640 110 L0 110 Z" fill="var(--grass-light)"/>
          <path d="M0 50 Q80 32 160 48 Q260 28 340 46 Q440 30 520 48 Q590 36 640 42 L640 110 L0 110 Z" fill="var(--grass)"/>
        </svg>
        <div class="footer__art" role="img" aria-label="Illustration of cartoon plush characters sitting on a green sofa"></div>
        <div class="ribbon">Happy kids in Nature | Happy kids in Ski</div>
        <p class="phone">
          <svg width="14" height="14" viewBox="0 0 24 24" aria-hidden="true"><path fill="#fff" d="M6.6 10.8a15.1 15.1 0 0 0 6.6 6.6l2.2-2.2a1 1 0 0 1 1-.25 11.4 11.4 0 0 0 3.6.57 1 1 0 0 1 1 1V20a1 1 0 0 1-1 1A17 17 0 0 1 3 4a1 1 0 0 1 1-1h3.5a1 1 0 0 1 1 1c0 1.25.2 2.45.57 3.6a1 1 0 0 1-.25 1z"/></svg>
          +49 (0) 170 5550 198
        </p>
      </footer>
    </div>
  </article>
</body>
</html>
```